Hardwood Flooring Company needs packaging design

We need a packaging design for our new product. We manufacture wood flooring and this year we are launching a new product that is high quality and superior durability and we want a design that communicate the superior quality of our product. We would like to see a nice design with colors shapes that communicates quality and fashion. The product carries warranty, so we need something like a 30 year warranty stamp on the box. Measurements of the box are 4” high (100mm) X 10” wide (250mm) x 84” long (2100mm).

Flooring

• 30 Year warranty stamp
• colors like blue or purple

```html
<!DOCTYPE html>
<html lang="en">
<head>
<meta charset="utf-8">
<title>Harven Flooring Box Dieline</title>
<link rel="stylesheet" href="https://fonts.googleapis.com/css2?family=Montserrat:wght@300;400;800&display=swap">
<style>
  :root {
    --orange: #e67826;
    --black: #000000;
    --white: #ffffff;
    --rule: #231f20;
  }
  html, body {
    margin: 0;
    padding: 0;
    width: 1200px;
    height: 848px;
    overflow: hidden;
    background: var(--white);
  }
  .dieline { display: block; width: 1200px; height: 848px; }
  .panel-frame { fill: var(--white); stroke: var(--rule); stroke-width: 1; }
  .panel-label { font-family: "Montserrat", sans-serif; font-weight: 400; font-size: 9px; fill: var(--rule); letter-spacing: 0.3px; }
  .brand { font-family: "Montserrat", sans-serif; font-weight: 800; }
  .brand-black { fill: var(--black); }
  .brand-orange { fill: var(--orange); }
  .brand-white { fill: var(--white); }
  .accent-bar { fill: var(--orange); }
  .bottom-band { fill: var(--black); }
  .bottom-rule { fill: var(--white); }
  .tagline { font-family: "Montserrat", sans-serif; font-weight: 400; font-size: 19px; fill: var(--orange); }
  .product-line { font-family: "Montserrat", sans-serif; font-weight: 400; font-size: 10.5px; fill: var(--orange); }
  .specs { font-family: "Montserrat", sans-serif; font-weight: 400; font-size: 6.5px; fill: var(--white); }
  .seal-placeholder { fill: var(--black); }
  .seal-caption { font-family: "Montserrat", sans-serif; font-weight: 400; font-size: 9px; fill: var(--rule); letter-spacing: 0.3px; }
</style>
</head>
<body>
<svg class="dieline" viewBox="0 0 1200 848" xmlns="http://www.w3.org/2000/svg">

  <g class="panel panel-back">
    <rect class="panel-frame" x="148.5" y="104.5" width="893" height="106"/>
    <text class="brand brand-black" x="384" y="192" font-size="101" textLength="643" lengthAdjust="spacingAndGlyphs">HARVEN</text>
    <text class="panel-label" x="149" y="229">BACK</text>
  </g>

  <g class="panel panel-top">
    <rect class="panel-frame" x="148.5" y="251.5" width="893" height="42"/>
    <rect class="accent-bar" x="149" y="260" width="655" height="25"/>
    <text class="tagline" x="1028" y="279" text-anchor="end">STRONG &amp; DURABLE</text>
    <text class="panel-label" x="149" y="312">TOP</text>
  </g>

  <g class="panel panel-front">
    <rect class="panel-frame" x="88.5" y="329.5" width="41" height="106"/>
    <text class="brand brand-black" font-size="10" text-anchor="middle" transform="translate(105 382) rotate(90)" textLength="54" lengthAdjust="spacingAndGlyphs">HARVEN</text>
    <rect class="panel-frame" x="1065.5" y="329.5" width="41" height="106"/>
    <text class="brand brand-black" font-size="10" text-anchor="middle" transform="translate(1090 382) rotate(-90)" textLength="54" lengthAdjust="spacingAndGlyphs">HARVEN</text>

    <rect class="panel-frame" x="148.5" y="329.5" width="893" height="106"/>
    <rect class="accent-bar" x="287" y="329" width="755" height="32"/>
    <circle class="seal-placeholder" cx="215" cy="383" r="42" role="img" aria-label="30 year warranty seal"/>
    <text class="brand brand-orange" x="750" y="405" font-size="40" textLength="272" lengthAdjust="spacingAndGlyphs">HARVEN</text>
    <text class="product-line" x="1024" y="423" text-anchor="end">WOOD FLOORING TILES (MAPLE WOOD FINISH)</text>
    <text class="panel-label" x="149" y="452">FRONT</text>
  </g>

  <g class="panel panel-bottom">
    <rect class="bottom-band" x="148" y="468" width="894" height="44"/>
    <text class="brand brand-white" x="163" y="495" font-size="15" textLength="97" lengthAdjust="spacingAndGlyphs">HARVEN</text>
    <rect class="bottom-rule" x="276" y="486" width="610" height="9"/>
    <text class="specs" x="1033" y="493" text-anchor="end" xml:space="preserve">SPECS: 84” x 10” x 3/4”    QTY: 10 PCS</text>
    <text class="panel-label" x="149" y="536">BOTTOM</text>
  </g>

  <g class="seal-spec">
    <circle class="seal-placeholder" cx="155" cy="686" r="61" role="img" aria-label="30 year warranty seal, spot UV black gloss"/>
    <text class="seal-caption" x="155" y="770" text-anchor="middle" xml:space="preserve">WARRANTY SEAL OF EXCELLENCE  &amp; QUALITY</text>
    <text class="seal-caption" x="155" y="786" text-anchor="middle">SPOT UV BLACK GLOSS TYPE</text>
  </g>

  <text class="brand brand-orange" x="943" y="806" font-size="29" textLength="194" lengthAdjust="spacingAndGlyphs">HARVEN</text>
</svg>
</body>
</html>
```